PowerPoint Design for a Biotech Consulting Firm

We need a powerpoint design for a new business based in Philadelphia called VentoraRx. This is a consulting firm that will serve medical diagnostics industry, which is part of the life science/healthcare industry focusing on developing and marketing products that help in early detection, monitoring or management of diseases. Our consulting firm will help medical diagnostic companies to overcome key challenges in designing, evaluating and marketing new products.Our company name is VentoraRx. Ventora is Latin word for "something", Dx represents diagnostics. The idea behind the name is that we help companies to transform the original, early product ideas ("nothing") into "something" which is a product with full clinical utility that will help to improve health and well-being.The powerpoint should use the visual feel of the logo (attached), be modern, simple and clean looking and represent creativity, innovation, scientific thinking and progress.

Target Market(s)

Biotech

Industry/Entity Type

Biotechnology

Font styles to use
Sans Serif

Colors
0355a3
3276b5
85abd2
cfdeed
ffffff
959595
aaaaaa
cbcbcb
070707

Requirements
Must have
• - look and feel, logo colors
• - multiple slide formats

```html
<!DOCTYPE html>
<html lang="en">
<head>
<meta charset="utf-8">
<title>VentoraRx – Consulting Firm Slide Set</title>
<link href="https://fonts.googleapis.com/css2?family=Archivo+Black&family=Jost:wght@300;400&family=Montserrat:wght@500&family=Roboto:wght@400&display=swap" rel="stylesheet">
<style>
  :root{
    --blue:#2d8cf0;
    --blue-deep:#1f6fd6;
    --steel:#4a7fc0;
    --ink:#1c1c1e;
    --text:#3e3e3e;
    --grey:#cbcbcb;
    --s1:#4764ad;
    --s2:#5b9bd5;
    --s3:#2e7fe0;
    --white:#ffffff;
  }
  *{margin:0;padding:0;box-sizing:border-box}
  html,body{width:686px;height:1200px;overflow:hidden;background:var(--white)}
  .canvas{position:relative;width:686px;height:1200px;background:var(--white);font-family:"Jost",sans-serif;color:var(--text)}
  .abs{position:absolute}
  .band{position:absolute;left:0;width:686px;background:var(--grey)}
  .line{position:absolute;background:var(--blue)}
  .gradient-bar{position:absolute;background:linear-gradient(90deg,#1b2230 0%,#1f6fd6 45%,#2d8cf0 60%,#3a8ff0 100%)}
  .steel-rule{position:absolute;background:var(--steel)}
  .fade-rule{position:absolute;background:linear-gradient(90deg,rgba(45,140,240,0) 0%,#2d8cf0 40%,#3c4a60 75%,rgba(45,140,240,0) 100%)}

  .brand{position:absolute;font-family:"Montserrat",sans-serif;font-weight:500;color:var(--ink);white-space:nowrap;line-height:1}

  .title-box{position:absolute;background:var(--ink);text-align:center}
  .title-main{font-family:"Archivo Black",sans-serif;font-size:38px;line-height:1;letter-spacing:.01em;color:var(--blue)}
  .title-main span{color:var(--white)}
  .title-sub{font-family:"Roboto",sans-serif;font-size:41px;line-height:1;color:var(--blue);margin-top:6px}
  .subtitle-box{position:absolute;background:var(--ink);text-align:center;color:#e8e8e8;font-weight:300;font-size:18px;padding-top:1px}

  .heading{position:absolute;font-weight:400;color:var(--ink);white-space:nowrap}
  .bullets{position:absolute;list-style:none;font-weight:300;color:var(--text)}
  .bullets li{position:relative;padding-left:6px}
  .bullets li::before{content:"";position:absolute;left:0;top:3px;width:2px;height:2px;background:var(--ink)}

  .divider-box{position:absolute;background:var(--blue);color:var(--white);font-weight:300}
  .para{position:absolute;font-weight:300;color:var(--text);font-size:11px;line-height:10.5px}
  svg text{font-family:"Jost",sans-serif}
</style>
</head>
<body>
<div class="canvas">

  <!-- Slide 1: cover -->
  <section class="cover">
    <div class="gradient-bar" style="left:13px;top:28px;width:124px;height:357px"></div>
    <div class="steel-rule" style="left:148px;top:28px;width:5px;height:357px"></div>
    <div class="fade-rule" style="left:0;top:266px;width:189px;height:4px"></div>
    <div class="brand" style="left:175px;top:67px;font-size:21px">VentoraRx</div>
    <div class="line" style="left:463px;top:29px;width:190px;height:4px"></div>
    <div class="line" style="left:629px;top:0;width:5px;height:149px"></div>
    <div class="title-box" style="left:160px;top:155px;width:474px;height:102px;padding-top:14px">
      <div class="title-main">VENTORA <span>RX</span></div>
      <div class="title-sub">CONSULTING FIRM</div>
    </div>
    <div class="subtitle-box" style="left:160px;top:278px;width:474px;height:72px">Click to add Subtitle</div>
  </section>

  <div class="band" style="top:385px;height:12px"></div>

  <!-- Slide 2: introduction -->
  <section class="intro">
    <div class="brand" style="left:14px;top:421px;font-size:7.5px">VentoraRx</div>
    <div class="line" style="left:56px;top:408px;width:287px;height:2px"></div>
    <div class="line" style="left:324px;top:397px;width:2px;height:181px"></div>
    <div class="line" style="left:16px;top:576px;width:309px;height:2px"></div>
    <div class="heading" style="left:58px;top:424px;font-size:17px">INTRODUCTION</div>
    <ul class="bullets" style="left:58px;top:453px;width:240px;font-size:8.3px;line-height:9px">
      <li style="margin-bottom:17px">Lorem ipsum dolor sit amet, consectetur adipiscing elit, sed do eiusmod tempor incididunt ut labore et dolore magna aliqua.</li>
      <li style="margin-bottom:17px">Lorem ipsum dolor sit amet, consectetur adipiscing elit, sed do eiusmod tempor incididunt ut labore et dolore magna aliqua.</li>
      <li>Lorem ipsum dolor sit amet, consectetur adipiscing elit, sed do eiusmod tempor incididunt ut labore et dolore magna aliqua.</li>
    </ul>
  </section>

  <!-- Slide 3: divider -->
  <section class="divider">
    <div class="gradient-bar" style="left:349px;top:411px;width:62px;height:178px"></div>
    <div class="steel-rule" style="left:417px;top:411px;width:3px;height:178px"></div>
    <div class="fade-rule" style="left:343px;top:484px;width:95px;height:2px"></div>
    <div class="line" style="left:575px;top:411px;width:94px;height:2px"></div>
    <div class="line" style="left:657px;top:397px;width:3px;height:74px"></div>
    <div class="divider-box" style="left:423px;top:416px;width:231px;height:63px;font-size:18px;padding:42px 0 0 2px;line-height:18px">This is a divider slide</div>
    <div class="divider-box" style="left:423px;top:491px;width:231px;height:33px;font-size:7.5px;padding:1px 0 0 2px">Write some introduction</div>
  </section>

  <div class="band" style="top:589px;height:10px"></div>

  <!-- Slide 4: two charts -->
  <section class="charts">
    <div class="brand" style="left:14px;top:625px;font-size:7.5px">VentoraRx</div>
    <div class="line" style="left:56px;top:611px;width:287px;height:2px"></div>
    <div class="line" style="left:324px;top:599px;width:2px;height:181px"></div>
    <div class="line" style="left:16px;top:779px;width:309px;height:2px"></div>

    <svg class="abs" style="left:50px;top:650px" width="140" height="124" viewBox="50 650 140 124" role="img" aria-label="Clustered column chart, three series across four categories">
      <text x="119" y="661" font-size="6" fill="#999" text-anchor="middle">Chart Title</text>
      <g stroke="#e4e4e4" stroke-width=".4">
        <line x1="64" x2="179" y1="753" y2="753"/><line x1="64" x2="179" y1="738.7" y2="738.7"/>
        <line x1="64" x2="179" y1="724.3" y2="724.3"/><line x1="64" x2="179" y1="710" y2="710"/>
        <line x1="64" x2="179" y1="695.7" y2="695.7"/><line x1="64" x2="179" y1="681.3" y2="681.3"/>
        <line x1="64" x2="179" y1="667" y2="667"/>
      </g>
      <g font-size="3.6" fill="#888" text-anchor="end">
        <text x="61" y="754">0</text><text x="61" y="740">1</text><text x="61" y="725.5">2</text>
        <text x="61" y="711">3</text><text x="61" y="697">4</text><text x="61" y="682.5">5</text><text x="61" y="668">6</text>
      </g>
      <g fill="var(--s1)"><rect x="70" y="691.4" width="4.5" height="61.6"/><rect x="99" y="717.2" width="4.5" height="35.8"/><rect x="128" y="702.8" width="4.5" height="50.2"/><rect x="157" y="688.5" width="4.5" height="64.5"/></g>
      <g fill="var(--s2)"><rect x="76.5" y="718.6" width="4.5" height="34.4"/><rect x="105.5" y="690" width="4.5" height="63"/><rect x="134.5" y="727.2" width="4.5" height="25.8"/><rect x="163.5" y="712.9" width="4.5" height="40.1"/></g>
      <g fill="var(--s3)"><rect x="83" y="724.3" width="4.5" height="28.7"/><rect x="112" y="724.3" width="4.5" height="28.7"/><rect x="141" y="710" width="4.5" height="43"/><rect x="170" y="681.3" width="4.5" height="71.7"/></g>
      <g font-size="3.6" fill="#888" text-anchor="middle">
        <text x="78" y="760">Category 1</text><text x="107" y="760">Category 2</text><text x="136" y="760">Category 3</text><text x="165" y="760">Category 4</text>
      </g>
      <g font-size="3.6" fill="#888">
        <rect x="88" y="765.3" width="2" height="2" fill="var(--s1)"/><text x="91" y="767.5">Series 1</text>
        <rect x="110" y="765.3" width="2" height="2" fill="var(--s2)"/><text x="113" y="767.5">Series 2</text>
        <rect x="132" y="765.3" width="2" height="2" fill="var(--s3)"/><text x="135" y="767.5">Series 3</text>
      </g>
    </svg>

    <svg class="abs" style="left:190px;top:650px" width="135" height="124" viewBox="190 650 135 124" role="img" aria-label="Three-dimensional column chart, three series across four categories">
      <text x="256" y="661" font-size="6" fill="#999" text-anchor="middle">Chart Title</text>
      <g stroke="#e4e4e4" stroke-width=".4" fill="none">
        <polyline points="204,737 214,729 300,729"/><polyline points="204,691 214,677 300,677"/>
        <line x1="214" y1="677" x2="214" y2="729"/>
      </g>
      <g font-size="3.6" fill="#888" text-anchor="end">
        <text x="198" y="739">0</text><text x="198" y="730">1</text><text x="198" y="721">2</text>
        <text x="198" y="711">3</text><text x="198" y="702">4</text><text x="198" y="693">5</text>
      </g>
      <g>
        <rect x="220" y="709" width="5" height="20" fill="var(--s3)"/><rect x="239" y="709" width="5" height="20" fill="var(--s3)"/>
        <rect x="258" y="699" width="5" height="30" fill="var(--s3)"/><rect x="281" y="679" width="8" height="50" fill="var(--s3)"/>
        <polygon points="281,679 284,677 292,677 289,679" fill="#6aa7ef"/><polygon points="289,679 292,677 292,727 289,729" fill="#1c5fb5"/>
      </g>
      <g fill="var(--s2)">
        <rect x="217" y="711" width="5" height="22"/><rect x="236" y="692" width="7" height="41"/>
        <rect x="256" y="716" width="5" height="17"/><rect x="276" y="704" width="5" height="29"/>
      </g>
      <g>
        <rect x="210" y="697" width="8" height="40" fill="var(--s1)"/><polygon points="210,697 213,695 221,695 218,697" fill="#7a90c8"/><polygon points="218,697 221,695 221,735 218,737" fill="#2f478a"/>
        <rect x="229" y="714" width="8" height="23" fill="var(--s1)"/><polygon points="229,714 232,712 240,712 237,714" fill="#7a90c8"/><polygon points="237,714 240,712 240,735 237,737" fill="#2f478a"/>
        <rect x="248" y="705" width="8" height="32" fill="var(--s1)"/><polygon points="248,705 251,703 259,703 256,705" fill="#7a90c8"/><polygon points="256,705 259,703 259,735 256,737" fill="#2f478a"/>
        <rect x="267" y="696" width="8" height="41" fill="var(--s1)"/><polygon points="267,696 270,694 278,694 275,696" fill="#7a90c8"/><polygon points="275,696 278,694 278,735 275,737" fill="#2f478a"/>
      </g>
      <g font-size="3.6" fill="#888" text-anchor="middle">
        <text x="212" y="746">Category</text><text x="212" y="750">1</text>
        <text x="231" y="746">Category</text><text x="231" y="750">2</text>
        <text x="250" y="746">Category</text><text x="250" y="750">3</text>
        <text x="269" y="746">Category</text><text x="269" y="750">4</text>
      </g>
      <g font-size="3.6" fill="#888"><text x="300" y="728">Series 3</text><text x="287" y="738">Series 1</text></g>
      <g font-size="3.6" fill="#888">
        <rect x="225" y="765.3" width="2" height="2" fill="var(--s1)"/><text x="228" y="767.5">Series 1</text>
        <rect x="247" y="765.3" width="2" height="2" fill="var(--s2)"/><text x="250" y="767.5">Series 2</text>
        <rect x="269" y="765.3" width="2" height="2" fill="var(--s3)"/><text x="272" y="767.5">Series 3</text>
      </g>
    </svg>
  </section>

  <!-- Slide 5: medical diagnostics -->
  <section class="diagnostics">
    <div class="brand" style="left:357px;top:625px;font-size:7.5px">VentoraRx</div>
    <div class="line" style="left:398px;top:611px;width:288px;height:2px"></div>
    <div class="line" style="left:667px;top:599px;width:2px;height:181px"></div>
    <div class="line" style="left:359px;top:779px;width:308px;height:2px"></div>
    <div class="heading" style="left:401px;top:628px;font-size:16.5px">MEDICAL DIAGNOSTICS</div>
    <ul class="bullets" style="left:401px;top:652px;width:132px;font-size:7px;line-height:7px">
      <li style="margin-bottom:14px">Lorem ipsum dolor sit amet, consectetuer adipiscing elit. Maecenas porttitor congue massa. Fusce posuere, magna sed pulvinar ultricies, purus lectus malesuada libero, sit amet commodo magna eros quis urna.</li>
      <li style="margin-bottom:14px">Nunc viverra imperdiet enim. Fusce est. Vivamus a tellus.</li>
      <li>Pellentesque habitant morbi tristique senectus et netus et malesuada fames ac turpis egestas. Proin pharetra nonummy pede. Mauris et orci.</li>
    </ul>
    <ul class="bullets" style="left:538px;top:652px;width:126px;font-size:7px;line-height:7px">
      <li style="margin-bottom:14px">Lorem ipsum dolor sit amet, consectetuer adipiscing elit. Maecenas porttitor congue massa. Fusce posuere, magna sed pulvinar ultricies, purus lectus malesuada libero, sit amet commodo magna eros quis urna.</li>
      <li style="margin-bottom:14px">Nunc viverra imperdiet enim. Fusce est. Vivamus a tellus.</li>
      <li>Pellentesque habitant morbi tristique senectus et netus et malesuada fames ac turpis egestas. Proin pharetra nonummy pede. Mauris et orci.</li>
    </ul>
  </section>

  <div class="band" style="top:792px;height:11px"></div>

  <!-- Slide 6: text and combo chart -->
  <section class="combo">
    <div class="brand" style="left:29px;top:852px;font-size:15px">VentoraRx</div>
    <div class="line" style="left:111px;top:826px;width:575px;height:5px"></div>
    <div class="line" style="left:648px;top:803px;width:5px;height:359px"></div>
    <div class="line" style="left:33px;top:1161px;width:615px;height:5px"></div>
    <div class="heading" style="left:117px;top:875px;font-size:23px">Lorem ipsum</div>
    <p class="para" style="left:117px;top:936px;width:148px">The quick brown fox jumps over the lazy dog. The quick brown fox jumps over the lazy dog.</p>
    <p class="para" style="left:117px;top:991px;width:148px">The quick brown fox jumps over the lazy dog. The quick brown fox jumps over the lazy dog.</p>
    <p class="para" style="left:117px;top:1047px;width:148px">The quick brown fox jumps over the lazy dog. The quick brown fox jumps over the lazy dog.</p>
    <p class="para" style="left:117px;top:1102px;width:148px">The quick brown fox jumps over the lazy dog. The quick brown fox jumps over the lazy dog.</p>

    <svg class="abs" style="left:275px;top:850px" width="370" height="300" viewBox="275 850 370 300" role="img" aria-label="Combined column and line chart, two column series and one line series on a secondary axis">
      <text x="457" y="866" font-size="13" fill="#999" text-anchor="middle" font-weight="300">Chart Title</text>
      <g stroke="#e2e2e2" stroke-width=".6">
        <line x1="301" x2="621" y1="1111" y2="1111"/><line x1="301" x2="621" y1="1087.8" y2="1087.8"/>
        <line x1="301" x2="621" y1="1064.6" y2="1064.6"/><line x1="301" x2="621" y1="1041.4" y2="1041.4"/>
        <line x1="301" x2="621" y1="1018.2" y2="1018.2"/><line x1="301" x2="621" y1="995" y2="995"/>
        <line x1="301" x2="621" y1="971.8" y2="971.8"/><line x1="301" x2="621" y1="948.6" y2="948.6"/>
        <line x1="301" x2="621" y1="925.4" y2="925.4"/><line x1="301" x2="621" y1="902.2" y2="902.2"/>
        <line x1="301" x2="621" y1="879" y2="879"/>
      </g>
      <g font-size="8.5" fill="#777" text-anchor="end" font-weight="300">
        <text x="294" y="1114">0</text><text x="294" y="1091">0.5</text><text x="294" y="1068">1</text>
        <text x="294" y="1044">1.5</text><text x="294" y="1021">2</text><text x="294" y="998">2.5</text>
        <text x="294" y="975">3</text><text x="294" y="952">3.5</text><text x="294" y="928">4</text>
        <text x="294" y="905">4.5</text><text x="294" y="882">5</text>
      </g>
      <g font-size="8.5" fill="#777" font-weight="300">
        <text x="629" y="1114">0</text><text x="629" y="1075">1</text><text x="629" y="1037">2</text>
        <text x="629" y="998">3</text><text x="629" y="959">4</text><text x="629" y="921">5</text><text x="629" y="882">6</text>
      </g>
      <g fill="var(--s1)">
        <rect x="321.5" y="911.5" width="18" height="199.5"/><rect x="401.1" y="995" width="18" height="116"/>
        <rect x="480.7" y="948.6" width="18" height="162.4"/><rect x="560.3" y="902.2" width="18" height="208.8"/>
      </g>
      <g fill="var(--s2)">
        <rect x="344.5" y="999.6" width="18" height="111.4"/><rect x="424.1" y="906.8" width="18" height="204.2"/>
        <rect x="503.7" y="1027.5" width="18" height="83.5"/><rect x="583.3" y="981.1" width="18" height="129.9"/>
      </g>
      <polyline points="341.5,1033.7 421.1,1033.7 500.7,995 580.3,919.7" fill="none" stroke="var(--s3)" stroke-width="1.4"/>
      <g font-size="8.5" fill="#777" text-anchor="middle" font-weight="300">
        <text x="342" y="1128">Category 1</text><text x="421" y="1128">Category 2</text>
        <text x="501" y="1128">Category 3</text><text x="580" y="1128">Category 4</text>
      </g>
      <g font-size="8.5" fill="#777" font-weight="300">
        <rect x="384" y="1137" width="14" height="5" fill="var(--s1)"/><text x="399" y="1143">Series 1</text>
        <rect x="437" y="1137" width="14" height="5" fill="var(--s2)"/><text x="452" y="1143">Series 2</text>
        <line x1="489" x2="504" y1="1139.5" y2="1139.5" stroke="var(--s3)" stroke-width="1.4"/><text x="505" y="1143">Series 3</text>
      </g>
    </svg>
  </section>

</div>
</body>
</html>
```